Flashy and colorful banner for an orange grower

Hi, I need a graphic for an advertising banner (80x200cm) to be placed next to the sales van. So far we have tried to highlight the naturalness of our products. With this banner we would like to highlight the ancient Sicilian tradition, with the typical decorations, I attach some photos as an example. We will sell our products far from Sicily, so I would like to exalt our origin.
We would like to dare with a colorful and amazing design, to capture the attention of passers-by.
It might be nice to insert or rework the decoration within our logo.
I would like to insert 4 of our offers inside the banner, only in the upper part, from the middle up.
The text is:
DAL CUORE DELLA SICILIA
ARANCIA TAROCCO
ALLA RINFUSA
5€ BORSA
DA SPREMERE
10€ CASSETTA
DA TAVOLA
15€ CASSETTA
SELEZIONE PREMIUM
20€ CASSETTA
Thanks for your time

```html
<!DOCTYPE html>
<html lang="it">
<head>
<meta charset="utf-8">
<title>Dal cuore della Sicilia – Arancia Tarocco</title>
<link rel="stylesheet" href="https://fonts.googleapis.com/css2?family=Lato:wght@700;900&display=swap">
<style>
  :root{
    --green:#146b3a;
    --green-deep:#0f5a30;
    --orange:#e2571d;
    --orange-light:#f39a2c;
    --gold:#f2d88b;
    --gold-deep:#e6c46a;
    --white:#ffffff;
    --page:#f1f1f1;
  }
  html,body{margin:0;padding:0;width:1200px;height:1200px;overflow:hidden;background:var(--page);}
  .banner{position:absolute;left:370px;top:25px;width:460px;height:1150px;
    box-shadow:0 6px 18px rgba(0,0,0,.12);}
  .banner svg{display:block;width:460px;height:1150px;}
  .headline{font-family:'Lato',sans-serif;font-weight:900;fill:var(--green);}
  .pill-text{font-family:'Lato',sans-serif;font-weight:900;fill:var(--white);}
  .offer-name{font-family:'Lato',sans-serif;font-weight:700;fill:var(--white);font-size:28px;}
  .offer-price{font-family:'Lato',sans-serif;font-weight:900;fill:var(--white);font-size:48px;}
  .offer-unit{font-family:'Lato',sans-serif;font-weight:700;fill:var(--white);font-size:15px;}
  .brand-name{font-family:'Lato',sans-serif;font-weight:900;fill:var(--green);font-size:44px;}
  .web{font-family:'Lato',sans-serif;font-weight:900;fill:var(--white);font-size:16px;letter-spacing:1px;}
  .divider{stroke:var(--white);stroke-width:2;stroke-dasharray:2 4;opacity:.85;}
</style>
</head>
<body>
<div class="banner">
<svg viewBox="0 0 460 1150" xmlns="http://www.w3.org/2000/svg">
  <defs>
    <radialGradient id="bodyGlow" cx="50%" cy="55%" r="60%">
      <stop offset="0" stop-color="#1a7a44"/>
      <stop offset="1" stop-color="#0f5a30"/>
    </radialGradient>
    <linearGradient id="borderTone" x1="0" y1="0" x2="1" y2="1">
      <stop offset="0" stop-color="#f2d88b"/>
      <stop offset=".5" stop-color="#e6c46a"/>
      <stop offset="1" stop-color="#f2d88b"/>
    </linearGradient>
    <radialGradient id="orangeTone" cx="50%" cy="50%" r="50%">
      <stop offset="0" stop-color="#f39a2c"/>
      <stop offset="1" stop-color="#e2571d"/>
    </radialGradient>
  </defs>

  <rect class="body-field" width="460" height="1150" fill="url(#bodyGlow)"/>

  <path class="header-field" d="M0,0 H460 V192 C340,250 150,256 0,180 Z" fill="var(--white)"/>
  <path class="header-swoosh" d="M0,182 C120,262 280,266 385,226 C260,286 100,272 0,226 Z" fill="var(--orange)"/>

  <text class="headline" x="262" y="92" font-size="52" text-anchor="end" textLength="192" lengthAdjust="spacingAndGlyphs">DAL CU</text>
  <circle class="heart-orange" cx="281" cy="74" r="19" fill="url(#orangeTone)" role="img" aria-label="Illustrazione di mezza arancia decorata al posto della O"/>
  <text class="headline" x="300" y="92" font-size="52" textLength="67" lengthAdjust="spacingAndGlyphs">RE</text>
  <text class="headline" x="226" y="145" font-size="52" text-anchor="middle" textLength="355" lengthAdjust="spacingAndGlyphs">DELLA SICILIA</text>
  <rect class="product-pill" x="56" y="158" width="342" height="34" rx="17" fill="var(--orange)"/>
  <text class="pill-text" x="227" y="185" font-size="27" text-anchor="middle" textLength="310" lengthAdjust="spacingAndGlyphs">ARANCIA TAROCCO</text>

  <g class="offers">
    <line class="divider" x1="253" y1="296" x2="253" y2="365"/>
    <text class="offer-name" x="80" y="316">ALLA</text>
    <text class="offer-name" x="80" y="351">RINFUSA</text>
    <text class="offer-price" x="326" y="338" text-anchor="middle">05€</text>
    <text class="offer-unit" x="326" y="362" text-anchor="middle">BORSA</text>
    <line class="divider" x1="74" y1="381" x2="374" y2="381"/>

    <line class="divider" x1="253" y1="399" x2="253" y2="468"/>
    <text class="offer-name" x="80" y="419">DA</text>
    <text class="offer-name" x="80" y="454">SPREMERE</text>
    <text class="offer-price" x="326" y="441" text-anchor="middle">10€</text>
    <text class="offer-unit" x="326" y="465" text-anchor="middle">CASSETTA</text>
    <line class="divider" x1="74" y1="484" x2="374" y2="484"/>

    <line class="divider" x1="253" y1="502" x2="253" y2="571"/>
    <text class="offer-name" x="80" y="522">DA</text>
    <text class="offer-name" x="80" y="557">TAVOLA</text>
    <text class="offer-price" x="326" y="544" text-anchor="middle">15€</text>
    <text class="offer-unit" x="326" y="568" text-anchor="middle">CASSETTA</text>
    <line class="divider" x1="74" y1="587" x2="374" y2="587"/>

    <line class="divider" x1="253" y1="605" x2="253" y2="674"/>
    <text class="offer-name" x="80" y="625">SELEZIONE</text>
    <text class="offer-name" x="80" y="660">PREMIUM</text>
    <text class="offer-price" x="326" y="647" text-anchor="middle">20€</text>
    <text class="offer-unit" x="326" y="671" text-anchor="middle">CASSETTA</text>
  </g>

  <path class="footer-swoosh" d="M60,1010 C200,900 340,850 460,860 V908 C320,890 190,930 60,1010 Z" fill="var(--orange)"/>
  <path class="footer-field" d="M0,1000 C140,920 300,885 460,905 V1150 H0 Z" fill="var(--white)"/>

  <g class="orange-illustration" role="img" aria-label="Illustrazione di mezza arancia con decorazioni siciliane e foglie">
    <ellipse cx="240" cy="765" rx="70" ry="40" fill="#3f9a3c"/>
    <circle cx="240" cy="857" r="128" fill="var(--white)"/>
    <circle cx="240" cy="857" r="114" fill="url(#orangeTone)"/>
  </g>

  <text class="brand-name" x="230" y="1050" text-anchor="middle">SOLEVERDE</text>

  <path class="web-plate" d="M80,1102 H380 L394,1128 H66 Z" fill="var(--green)"/>
  <text class="web" x="230" y="1121" text-anchor="middle" textLength="280" lengthAdjust="spacingAndGlyphs">WWW.SOLEVERDE-AGRUMI.COM</text>

  <g class="frame-ornament" role="img" aria-label="Cornice decorativa in stile carretto siciliano">
    <path d="M0,0 H460 V200 H438 V22 H22 V192 H0 Z" fill="url(#borderTone)"/>
    <path d="M0,1012 H22 V1128 H438 V910 H460 V1150 H0 Z" fill="url(#borderTone)"/>
    <path d="M22,22 H438 V200 H432 V28 H28 V188 H22 Z" fill="var(--orange)"/>
    <path d="M22,1008 H28 V1122 H432 V912 H438 V1128 H22 Z" fill="var(--orange)"/>
  </g>
</svg>
</div>
</body>
</html>
```